Pediatric Practice Flyer Design

I need marketing flyer created for distribution. It is for a pediatric clinic. Need some realistic eye catching design and content. I already have a logo that will go on top of the flyer. I will be using corbelwade for flyer print service. So need it copyable for printing. Again, need eye catching content as well. We are planning on opening the clinic in December.

```html
<!DOCTYPE html>
<html lang="en">
<head>
<meta charset="utf-8">
<title>Pediatric Clinic Opening Flyer</title>
<link rel="stylesheet" href="https://fonts.googleapis.com/css2?family=Bebas+Neue&family=Kaushan+Script&family=Roboto:ital,wght@0,400;0,500;0,700;1,500&display=swap">
<style>
  :root {
    --page-bg: #d4d4d4;
    --paper: #ffffff;
    --paper-shade: #ececec;
    --ink: #1b1b1b;
    --red: #e0222c;
    --blue: #1a6fb5;
    --orange: #ec9024;
    --teal: #1fa394;
    --purple: #6a2e92;
    --photo-a: #c9c2bd;
    --photo-b: #8d93b8;
  }
  * { margin: 0; padding: 0; box-sizing: border-box; }
  html, body { width: 1107px; height: 1200px; overflow: hidden; }
  body { background: var(--page-bg); font-family: "Roboto", sans-serif; position: relative; }

  .flyer {
    position: absolute; left: 164px; top: 43px; width: 778px; height: 1114px;
    background: linear-gradient(180deg, var(--paper) 40%, var(--paper-shade) 100%);
    overflow: hidden;
  }
  .flyer-art { position: absolute; inset: 0; }

  .badge-free {
    position: absolute; left: 40px; top: 254px; width: 160px; text-align: center; color: #fff;
  }
  .badge-free .big { font-family: "Bebas Neue", sans-serif; font-size: 68px; line-height: 1; display: block; }
  .badge-free .small { font-size: 11px; font-weight: 500; letter-spacing: .2px; display: block; margin-top: -4px; }

  .headline { position: absolute; left: 72px; top: 430px; }
  .headline .coming {
    font-family: "Kaushan Script", cursive; font-size: 66px; color: var(--ink); line-height: 1;
  }
  .headline .title {
    font-family: "Bebas Neue", sans-serif; font-size: 118px; color: var(--red);
    line-height: .9; margin-top: 14px; letter-spacing: -1px;
  }
  .headline .subtitle {
    font-size: 32px; font-weight: 500; color: var(--ink); margin-top: 10px; letter-spacing: .2px;
  }

  .services {
    position: absolute; left: 56px; top: 731px; width: 660px;
    display: flex; justify-content: space-between; list-style: none;
  }
  .service { width: 164px; display: flex; flex-direction: column; align-items: center; }
  .service-icon {
    width: 108px; height: 108px; border-radius: 50%;
    display: flex; align-items: center; justify-content: center;
  }
  .service-icon.teal { background: var(--teal); }
  .service-icon.red { background: var(--red); }
  .service-icon.purple { background: var(--purple); }
  .service-icon.orange { background: var(--orange); }
  .service-label {
    margin-top: 26px; font-size: 21px; font-weight: 500; text-align: center;
    line-height: 1.25; color: var(--ink); text-transform: uppercase;
  }

  .brand { position: absolute; left: 72px; top: 972px; display: flex; align-items: center; gap: 12px; }
  .brand-dot { width: 44px; height: 44px; border-radius: 50%; background: var(--red); }
  .brand-name { font-size: 26px; font-weight: 700; color: var(--red); }

  .contact { position: absolute; left: 434px; top: 956px; color: var(--ink); }
  .contact .web { font-size: 20px; font-weight: 700; color: var(--red); }
  .contact .line { font-size: 14.5px; margin-top: 6px; }

  .address-band {
    position: absolute; left: 0; bottom: 8px; width: 100%; height: 49px;
    background: var(--blue); color: #fff; display: flex; align-items: center; justify-content: center;
    font-size: 17px; font-style: italic; font-weight: 500;
  }
  .address-rule { position: absolute; left: 0; bottom: 0; width: 100%; height: 8px; background: var(--orange); }
</style>
</head>
<body>
<main class="flyer">
  <svg class="flyer-art" viewBox="0 0 778 1114" width="778" height="1114">
    <defs>
      <linearGradient id="heroTone" x1="0" y1="0" x2="1" y2="1">
        <stop offset="0" stop-color="var(--photo-a)"/>
        <stop offset="1" stop-color="var(--photo-b)"/>
      </linearGradient>
      <linearGradient id="insetTone" x1="0" y1="0" x2="1" y2="1">
        <stop offset="0" stop-color="#b9a08f"/>
        <stop offset="1" stop-color="#4b4470"/>
      </linearGradient>
    </defs>
    <rect class="hero-photo" x="0" y="0" width="778" height="400" fill="url(#heroTone)" role="img" aria-label="Photo of a mother holding her baby while a smiling pediatrician greets them"/>
    <path class="hero-curve" d="M0,244 C120,330 240,372 340,364 C470,352 600,200 705,0 L778,0 L778,1114 L0,1114 Z" fill="#fff"/>
    <path class="stripe-red" d="M330,365 C470,350 600,190 690,0 L778,0 L778,30 C700,160 560,330 330,365 Z" fill="var(--red)"/>
    <path class="stripe-blue" d="M598,278 C660,210 720,120 778,55 L778,88 C728,150 676,215 628,272 Z" fill="var(--blue)"/>
    <path class="panel-orange" d="M640,280 C690,220 735,160 778,108 L778,590 L650,500 Z" fill="var(--orange)"/>
    <circle cx="608" cy="404" r="126" fill="#fff"/>
    <circle class="inset-photo" cx="608" cy="404" r="118" fill="url(#insetTone)" role="img" aria-label="Photo of a doctor examining a baby with a stethoscope"/>
    <g stroke="#fff" stroke-width="6" stroke-linecap="round">
      <line x1="48" y1="212" x2="76" y2="222"/><line x1="66" y1="194" x2="84" y2="214"/><line x1="86" y1="188" x2="90" y2="210"/>
    </g>
    <g stroke="#fff" stroke-width="6" stroke-linecap="round">
      <line x1="702" y1="268" x2="708" y2="290"/><line x1="716" y1="280" x2="720" y2="295"/><line x1="722" y1="298" x2="742" y2="300"/>
    </g>
    <g class="badge-shape" fill="var(--orange)">
      <circle cx="120" cy="304" r="62"/>
      <circle cx="120" cy="244" r="24"/><circle cx="176" cy="270" r="24"/><circle cx="180" cy="330" r="24"/>
      <circle cx="124" cy="364" r="24"/><circle cx="64" cy="338" r="24"/><circle cx="62" cy="276" r="24"/>
    </g>
  </svg>

  <div class="badge-free"><span class="big">FREE</span><span class="small">1ST CONSULTATION</span></div>

  <section class="headline">
    <p class="coming">Coming Soon</p>
    <h1 class="title">PEDIATRICIAN</h1>
    <p class="subtitle">ACCEPTING NEW PATIENTS</p>
  </section>

  <ul class="services">
    <li class="service">
      <div class="service-icon teal">
        <svg width="60" height="60" viewBox="0 0 60 60" fill="none" stroke="#fff" stroke-width="3" stroke-linejoin="round">
          <rect x="6" y="16" width="48" height="34" rx="5"/><path d="M22 16 V10 H38 V16"/><path d="M30 25 V41 M22 33 H38" stroke-linecap="round"/>
        </svg>
      </div>
      <p class="service-label">24/7<br>Service</p>
    </li>
    <li class="service">
      <div class="service-icon red">
        <svg width="70" height="60" viewBox="0 0 70 60" fill="none" stroke="#fff" stroke-width="3" stroke-linejoin="round">
          <rect x="26" y="8" width="38" height="36" rx="3"/><path d="M26 20 H14 L5 32 V44 H26"/><circle cx="16" cy="46" r="6" fill="var(--red)"/><circle cx="52" cy="46" r="6" fill="var(--red)"/><path d="M45 16 V36 M35 26 H55" stroke-linecap="round"/>
        </svg>
      </div>
      <p class="service-label">Emergency<br>Service</p>
    </li>
    <li class="service">
      <div class="service-icon purple">
        <svg width="60" height="60" viewBox="0 0 60 60" fill="none" stroke="#fff" stroke-width="3" stroke-linejoin="round">
          <path d="M6 28 L30 8 L54 28"/><path d="M12 24 V52 H48 V24"/><path d="M30 22 V40 M21 31 H39" stroke-linecap="round"/>
        </svg>
      </div>
      <p class="service-label">Good<br>Care</p>
    </li>
    <li class="service">
      <div class="service-icon orange">
        <svg width="60" height="60" viewBox="0 0 60 60" fill="none" stroke="#fff" stroke-width="3" stroke-linecap="round">
          <path d="M12 6 V24 A12 12 0 0 0 36 24 V6"/><path d="M24 36 V42 A10 10 0 0 0 44 42 V34"/><circle cx="44" cy="28" r="6"/>
        </svg>
      </div>
      <p class="service-label">Consultancy<br>Service</p>
    </li>
  </ul>

  <div class="brand"><span class="brand-dot"></span><span class="brand-name">Maple Sprout Pediatrics</span></div>

  <div class="contact">
    <p class="web">www.maplesproutkids.com</p>
    <p class="line">Ph: 919-555-0142. Fax: 919-555-0187</p>
    <p class="line">office@maplesproutkids.com</p>
  </div>

  <div class="address-band">48 Linden Park Rd, Suite 12, Cary NC 27511</div>
  <div class="address-rule"></div>
</main>
</body>
</html>
```